The Quiet Hinge Mending Ledger

I am making a journal for tracking pain symptoms for TMJ (Jaw) pain. I have the cover designed and I just need the journal page designed that will repeat throughout the journal. The journal is the image on the left of the bundle. The page I would like to be developed is the picture that I hand sketched out. It should be a 6 x 9 page, similar to the attached example. Greyscale, no color. Thank you!

Target Market(s)

20-55 year old women

Industry/Entity Type

Healthcare

Colors

Designer to choose only greyscale colors for use in the design.

Requirements
Must have
• A neat, well-designed page with the content I have sketched out by hand.
Nice to have
• Creative display of the content I provided and development of the pain scale and pain diagram faces in a professional looking way.

```html
<!DOCTYPE html>
<html lang="en">
<head>
<meta charset="utf-8">
<title>The Quiet Hinge Mending Ledger – Daily Page</title>
<link href="https://fonts.googleapis.com/css2?family=Fira+Sans:wght@400;600&family=Fira+Sans+Condensed:wght@400;500&display=swap" rel="stylesheet">
<style>
:root{
  --ink:#1a1a1a;
  --bar-dark:#8e8d8f;
  --cell-head:#5b5b5d;
  --cell-row1:#8e8d8f;
  --cell-row2:#c0bfbe;
  --bar-light:#c4c4c4;
  --box-light:#f0eff0;
  --box-mid:#bdbdbd;
  --art:#b9b9b9;
  --paper:#ffffff;
  --brand:#6a6a6a;
}
*{box-sizing:border-box;margin:0;padding:0}
html,body{width:800px;height:1200px;overflow:hidden;background:var(--paper)}
body{font-family:"Fira Sans",sans-serif;color:var(--ink);position:relative}
.abs{position:absolute}
.brand{left:40px;top:44px;display:flex;align-items:center;gap:10px}
.brand-dot{width:62px;height:62px;border-radius:50%;background:var(--brand)}
.brand-name{font-family:"Fira Sans",sans-serif;font-weight:600;color:var(--brand);font-size:15px;line-height:18px;width:120px}
.field{font-family:"Fira Sans",sans-serif;font-size:23px;top:96px;display:flex;align-items:flex-end}
.field .rule{display:inline-block;border-bottom:1.5px solid var(--ink);height:22px;margin-left:2px}
.bar{left:27px;width:745px;height:36px;border-radius:18px;background:var(--bar-dark);
  font-family:"Fira Sans Condensed",sans-serif;font-size:23px;text-align:center;line-height:36px}
.bar.light{background:var(--bar-light)}
.time-table{left:50px;top:176px;width:701px;border-collapse:separate;border-spacing:3px;
  font-family:"Fira Sans Condensed",sans-serif}
.time-table th{background:var(--cell-head);color:#fff;font-weight:400;font-size:22px;height:33px}
.time-table td{height:34px;font-size:20px;text-align:center}
.time-table .r1 td{background:var(--cell-row1)}
.time-table .r2 td{background:var(--cell-row2)}
.time-table th.idx,.time-table td.idx{width:48px}
.scale-num{top:343px;font-size:19px;width:30px;text-align:center;margin-left:-15px}
.scale-face{top:374px;width:78px;height:78px;border-radius:50%;border:2px solid var(--ink);background:#e4e4e4}
.scale-label{top:456px;font-family:"Fira Sans Condensed",sans-serif;font-size:17px;width:160px;text-align:center;margin-left:-80px}
.loc-art{top:536px;height:92px;background:radial-gradient(circle at 55% 50%,#9a9a9a,#dcdcdc 70%);border-radius:8px}
.loc-label{top:628px;font-family:"Fira Sans Condensed",sans-serif;font-size:15px;width:90px;text-align:center;margin-left:-45px}
.joint-box{left:439px;top:526px;width:320px;height:118px;background:var(--box-mid)}
.joint-head{height:27px;background:#9f9f9f;display:flex;justify-content:space-between;padding:0 8px 0 14px;
  font-family:"Fira Sans Condensed",sans-serif;font-size:20px;line-height:28px}
.joint-cols{display:flex;padding:3px 0 0 14px}
.joint-cols ul{list-style:none;width:162px}
.opt{font-size:17px;line-height:25px;white-space:nowrap}
.box{display:inline-block;width:12px;height:12px;border:1.5px solid var(--ink);border-radius:2px;margin-right:5px;vertical-align:-1px}
.check-panel{left:42px;width:716px;background:var(--box-light);display:grid;grid-template-columns:247px 247px 1fr;padding:6px 0 0 15px}
.check-panel ul{list-style:none}
.check-panel .opt{line-height:22px}
.blank{display:inline-block;border-bottom:1.2px solid var(--ink);vertical-align:-2px}
.state-row{left:42px;font-size:17px;white-space:nowrap}
.state-row .opt{margin-right:22px}
.note-line{left:42px;width:716px;border-top:1.2px solid var(--ink)}
</style>
</head>
<body>

<div class="abs brand">
  <span class="brand-dot" aria-hidden="true"></span>
  <span class="brand-name">The Quiet Hinge Mending Ledger</span>
</div>
<div class="abs field" style="left:245px">DATE<span class="rule" style="width:95px"></span></div>
<div class="abs field" style="left:446px">DAY OF THE WEEK<span class="rule" style="width:107px"></span></div>

<div class="abs bar" style="top:137px">TIME</div>
<table class="abs time-table">
  <tr><th class="idx"></th><th>begin</th><th>end</th><th>duration</th><th class="idx"></th><th>begin</th><th>end</th><th>duration</th></tr>
  <tr class="r1"><td class="idx">1</td><td></td><td></td><td></td><td class="idx">3</td><td></td><td></td><td></td></tr>
  <tr class="r2"><td class="idx">2</td><td></td><td></td><td></td><td class="idx">4</td><td></td><td></td><td></td></tr>
</table>

<div class="abs bar" style="top:305px">SEVERITY OF PAIN (circle range)</div>
<span class="abs scale-num" style="left:106px">1</span>
<span class="abs scale-num" style="left:174px">2</span>
<span class="abs scale-num" style="left:237px">3</span>
<span class="abs scale-num" style="left:300px">4</span>
<span class="abs scale-num" style="left:364px">5</span>
<span class="abs scale-num" style="left:428px">6</span>
<span class="abs scale-num" style="left:491px">7</span>
<span class="abs scale-num" style="left:555px">8</span>
<span class="abs scale-num" style="left:619px">9</span>
<span class="abs scale-num" style="left:687px">10</span>
<div class="abs scale-face" style="left:95px" role="img" aria-label="Pain scale icon: no pain, smiling"></div>
<div class="abs scale-face" style="left:203px" role="img" aria-label="Pain scale icon: mild pain"></div>
<div class="abs scale-face" style="left:311px" role="img" aria-label="Pain scale icon: moderate pain"></div>
<div class="abs scale-face" style="left:419px" role="img" aria-label="Pain scale icon: severe pain"></div>
<div class="abs scale-face" style="left:527px" role="img" aria-label="Pain scale icon: very severe pain"></div>
<div class="abs scale-face" style="left:635px" role="img" aria-label="Pain scale icon: worst pain possible, tearful"></div>
<span class="abs scale-label" style="left:241px">mild</span>
<span class="abs scale-label" style="left:349px">moderate</span>
<span class="abs scale-label" style="left:460px">severe</span>
<span class="abs scale-label" style="left:566px">very severe</span>
<span class="abs scale-label" style="left:684px">worst pain possible</span>

<div class="abs bar" style="top:485px">LOCATION (circle)</div>
<div class="abs loc-art" style="left:36px;width:70px" role="img" aria-label="Head profile with jaw joint highlighted"></div>
<div class="abs loc-art" style="left:118px;width:56px" role="img" aria-label="Face with jaw muscles highlighted"></div>
<div class="abs loc-art" style="left:192px;width:66px" role="img" aria-label="Head with neck area highlighted"></div>
<div class="abs loc-art" style="left:270px;width:60px" role="img" aria-label="Face with forehead tension highlighted"></div>
<div class="abs loc-art" style="left:339px;width:91px" role="img" aria-label="Upper and lower rows of teeth"></div>
<span class="abs loc-label" style="left:64px">tmj</span>
<span class="abs loc-label" style="left:144px">muscles</span>
<span class="abs loc-label" style="left:228px">neck</span>
<span class="abs loc-label" style="left:300px">tension</span>
<span class="abs loc-label" style="left:385px">teeth</span>

<div class="abs joint-box">
  <div class="joint-head"><span>CLICK/POP</span><span>OPENING ABILITY</span></div>
  <div class="joint-cols">
    <ul><li class="opt"><span class="box"></span>increased</li><li class="opt"><span class="box"></span>decreased</li><li class="opt"><span class="box"></span>no change</li></ul>
    <ul><li class="opt"><span class="box"></span>increased</li><li class="opt"><span class="box"></span>decreased</li><li class="opt"><span class="box"></span>no change</li></ul>
  </div>
</div>

<div class="abs bar light" style="top:655px">TRIGGERS (check all that apply)</div>
<div class="abs check-panel" style="top:694px;height:102px">
  <ul><li class="opt"><span class="box"></span>Sleep</li><li class="opt"><span class="box"></span>First thing in AM</li><li class="opt"><span class="box"></span>Clenching/Grinding</li><li class="opt"><span class="box"></span>Insomnia</li></ul>
  <ul><li class="opt"><span class="box"></span>Weather</li><li class="opt"><span class="box"></span>Eating</li><li class="opt"><span class="box"></span>Work</li><li class="opt"><span class="box"></span>Opening wide/yawn</li></ul>
  <ul><li class="opt"><span class="box"></span>PMS/menstruation</li><li class="opt"><span class="box"></span>Stress at home</li><li class="opt"><span class="box"></span>Stress at work</li><li class="opt"><span class="box"></span>Other<span class="blank" style="width:104px"></span></li></ul>
</div>

<div class="abs state-row" style="top:802px">My jaw was <span class="opt"><span class="box"></span>relaxed</span><span class="opt"><span class="box"></span>clenched</span><span class="opt"><span class="box"></span>tense</span></div>
<div class="abs state-row" style="top:828px">My breathing was <span class="opt"><span class="box"></span>deep / relaxed</span><span class="opt"><span class="box"></span>shallow / tense</span></div>
<div class="abs state-row" style="top:853px">My neck / shoulders were <span class="opt"><span class="box"></span>relaxed</span><span class="opt"><span class="box"></span>tense</span><span class="opt"><span class="box"></span>slouched</span><span class="opt"><span class="box"></span>upright</span></div>

<div class="abs bar light" style="top:880px">RELIEF MEASURES (check all that apply)</div>
<div class="abs check-panel" style="top:920px;height:98px">
  <ul><li class="opt"><span class="box"></span>Deep breathing</li><li class="opt"><span class="box"></span>Teeth apart/relax jaw</li><li class="opt"><span class="box"></span>Self-massage</li><li class="opt"><span class="box"></span>Heat/cold (circle)</li></ul>
  <ul><li class="opt"><span class="box"></span>Medication</li><li class="opt"><span class="box"></span>Rest</li><li class="opt"><span class="box"></span>Gentle Stretching</li><li class="opt"><span class="box"></span>Posture correction</li></ul>
  <ul><li class="opt"><span class="box"></span>Mindful reset</li><li class="opt"><span class="box"></span>Stabilization Exercise</li><li class="opt"><span class="box"></span>Other<span class="blank" style="width:120px"></span></li><li class="opt"><span class="box"></span><span class="blank" style="width:168px"></span></li></ul>
</div>

<div class="abs bar light" style="top:1027px">NOTES AND PLAN TO AVOID TRIGGERS</div>
<div class="abs note-line" style="top:1092px"></div>
<div class="abs note-line" style="top:1119px"></div>
<div class="abs note-line" style="top:1145px"></div>
<div class="abs note-line" style="top:1172px"></div>

</body>
</html>
```